Packaging and Logo for upscale skincare line

The name of the brand is Rosalind Rosalind. We would like a logo that's a mirror image of there name Rosalind. Packaging design for three signature products, face cream, body cream, and an aerosol spf. The face cream should be about 1/3 of the size of the body cream, in similarly shaped containers with twist-off lids, and a spatula for the face cream. And the spf should be a taller, slimmer, bottle with removable cap and aerosol spray.
Updates

Low design quality

Industry/Entity Type

Skin Care

Logo Text

Rosalind

Colors
2a71b2
3176b5
85acd3
ffffff

Requirements
Must have
• N/A
Nice to have
• Would like the logo Rosalind Rosalind to be a single Rosalind in a mirror image. We also want the packaging to are in a deep blue ocean color with either a chrome or satin finish and the logo/wording on it to be almost like a pearl color. See colors attached.

```html
<!DOCTYPE html>
<html lang="en">
<head>
<meta charset="utf-8">
<title>Rosalind Face Cream – Packaging Front</title>
<link rel="stylesheet" href="https://fonts.googleapis.com/css2?family=Lato:wght@300;400&family=Source+Serif+4:wght@400&display=swap">
<style>
  :root {
    --backdrop: #efefef;
    --carton-white: #ffffff;
    --lid-edge: #e6e6e6;
    --ocean-blue: #2a6eb0;
    --pearl: #ffffff;
    --dot-tone-a: #5e93c9;
    --dot-tone-b: #3f7cbc;
  }
  * { margin: 0; padding: 0; box-sizing: border-box; }
  html, body {
    width: 1200px;
    height: 1200px;
    overflow: hidden;
    background: var(--backdrop);
  }
  .canvas {
    position: relative;
    width: 1200px;
    height: 1200px;
  }
  .carton-front {
    position: absolute;
    left: 118px;
    top: 60px;
    width: 964px;
    height: 1056px;
    background: var(--carton-white);
    border-radius: 6px;
    overflow: hidden;
  }
  .lid-seam {
    position: absolute;
    left: 0;
    right: 0;
    top: 990px;
    height: 2px;
    background: var(--lid-edge);
  }
  .brand-band {
    position: absolute;
    left: 0;
    right: 0;
    top: 432px;
    height: 552px;
    background: var(--ocean-blue);
  }
  .brand-name {
    position: absolute;
    left: 0;
    right: 0;
    top: 70px;
    text-align: center;
    font-family: "Lato", sans-serif;
    font-weight: 300;
    font-size: 92px;
    letter-spacing: 2px;
    color: var(--pearl);
    line-height: 1;
  }
  .band-divider {
    position: absolute;
    left: 0;
    right: 0;
    top: 206px;
    height: 4px;
    background: var(--pearl);
  }
  .product-name {
    position: absolute;
    left: 0;
    right: 0;
    top: 294px;
    text-align: center;
    font-family: "Lato", sans-serif;
    font-weight: 300;
    font-size: 38px;
    letter-spacing: 5px;
    color: var(--pearl);
  }
  .product-benefits {
    position: absolute;
    left: 0;
    right: 0;
    top: 360px;
    text-align: center;
    font-family: "Source Serif 4", serif;
    font-size: 19px;
    color: var(--pearl);
  }
  .product-benefits .separator {
    display: inline-block;
    width: 6px;
    height: 6px;
    margin: 0 9px 3px;
    border-radius: 50%;
    background: var(--pearl);
    vertical-align: middle;
  }
  .dot-texture {
    position: absolute;
    left: 0;
    bottom: 0;
    width: 196px;
    height: 216px;
    background: linear-gradient(135deg, var(--dot-tone-a), var(--dot-tone-b));
    opacity: 0.7;
  }
</style>
</head>
<body>
  <main class="canvas">
    <section class="carton-front">
      <div class="brand-band">
        <h1 class="brand-name">Rosalind</h1>
        <div class="band-divider"></div>
        <h2 class="product-name">Face Cream</h2>
        <p class="product-benefits">Purify<span class="separator"></span>Detox<span class="separator"></span>moisturize</p>
        <div class="dot-texture" role="img" aria-label="Decorative pattern of soft light-blue dots"></div>
      </div>
      <div class="lid-seam"></div>
    </section>
  </main>
</body>
</html>
```